Plumvale CEO needs a Crowdsourced Graphic for a Wirelark Article

I need a simple graphic / banner for a blog post that's going to be posted on Wirelark (www.wirelark.com) - the biggest tech blog in the world.

The article will be written by Tobin Marsh (Plumvale's CEO) and the title will be "Asia's Secret Crowdsourcing Boom". The article is about the tens of thousands of people using crowdsourcing websites (like Plumvale.com, Qorvel.com and Vantrio.com) in China, India, the Philippines, Australia and other countries in the Asia Pacific region.

We'd really like to get this ASAP - so early submissions encouraged. We will try and get the winning designer linked to from the article.

Thanks to everyone that submitted!  Some great designs and hard to choose! :)

Target Market(s)

Tech saavy readers, English speakers

Industry/Entity Type

Tech

Requirements
Must have
• The graphic SHOULD:
1) Have the text "Asia's secret crowdsourcing boom" with some nice design and fonts (consider grey subtle pattern background and white drop shadow on fonts) - see attached examples
2) Have an Asian theme
3) Have the dimensions 640px wide by 240px wide
Nice to have
• The graphic COULD:
1) Have references to some or all of the countries mentioned above or use Asian characters as part of the background / motif (maybe the word "crowd" or "crowd sourcing" in different languages). In Chinese, the word for crowdsourcing is "witkey" (and there are corresponding Chinese characters: ??)
2) Emphasize the word "Asia" (using color and larger/different font)
3) Use a chart showing exponential (i.e. fast) growth - like the attached
4) Have a second line of text "5 Things You Didn't Know About Crowdsourcing in Asia"

```html
<!DOCTYPE html>
<html lang="en">
<head>
<meta charset="UTF-8">
<title>Asia's Secret Crowdsourcing Boom</title>
<link href="https://fonts.googleapis.com/css2?family=Gelasio:wght@400&family=Questrial&family=Noto+Sans+SC:wght@400&family=Noto+Sans+Devanagari:wght@400&display=swap" rel="stylesheet">
<style>
  :root {
    --bg-light: #f1f1f1;
    --bg-mid: #e2e2e2;
    --motif: #cfcfcf;
    --motif-dark: #bdbdbd;
    --brand-red: #b5121b;
    --ink: #333333;
    --frame: #6a6a6a;
    --chart-fill-top: #c4c8d6;
    --chart-fill-bottom: #dfe1ea;
    --white: #ffffff;
  }
  * { margin: 0; padding: 0; box-sizing: border-box; }
  html, body { width: 1200px; height: 450px; overflow: hidden; }
  body { background: var(--white); }
  .banner {
    position: relative;
    width: 1200px;
    height: 450px;
    overflow: hidden;
    background:
      repeating-linear-gradient(45deg, rgba(255,255,255,0.35) 0 2px, transparent 2px 5px),
      radial-gradient(ellipse at 40% 40%, var(--bg-light) 0%, var(--bg-mid) 100%);
  }
  .motif-word {
    position: absolute;
    color: var(--motif);
    white-space: nowrap;
    line-height: 1;
  }
  .motif-word.latin { font-family: "Questrial", sans-serif; font-weight: 700; }
  .motif-word.hindi { font-family: "Noto Sans Devanagari", sans-serif; }
  .motif-word.hanzi { font-family: "Noto Sans SC", sans-serif; }
  .hands-area {
    position: absolute;
    left: 740px; top: 0;
    width: 460px; height: 310px;
    background: radial-gradient(ellipse at 55% 45%, rgba(150,150,150,0.45) 0%, rgba(170,170,170,0.2) 50%, rgba(220,220,220,0) 75%);
  }
  .emblem {
    position: absolute;
    left: 9px; top: 51px;
    width: 180px; height: 180px;
    border-radius: 50%;
    background: radial-gradient(circle, #ffffff 0%, #9a9a9a 45%, #5a5a5a 70%, #e6e6e6 100%);
  }
  .chart { position: absolute; inset: 0; }
  .title {
    position: absolute;
    font-family: "Gelasio", Georgia, serif;
    color: var(--brand-red);
    text-shadow: 2px 2px 0 var(--white);
    line-height: 1;
    white-space: nowrap;
  }
  .title-main { left: 238px; top: 42px; font-size: 134px; letter-spacing: -1px; }
  .title-sub { left: 242px; top: 170px; font-size: 58px; }
  .subtitle-box {
    position: absolute;
    left: 219px; top: 240px;
    width: 692px; height: 56px;
    border: 2px solid var(--frame);
    border-radius: 12px;
    background: rgba(255,255,255,0.9);
    display: flex;
    align-items: center;
  }
  .subtitle-number {
    width: 58px; height: 100%;
    border-right: 2px solid var(--frame);
    display: flex; align-items: center; justify-content: center;
    font-family: "Questrial", sans-serif;
    font-size: 40px;
    color: var(--ink);
  }
  .subtitle-text {
    padding-left: 12px;
    font-family: "Questrial", sans-serif;
    font-size: 25px;
    letter-spacing: 0.3px;
    color: var(--ink);
    white-space: nowrap;
  }
</style>
</head>
<body>
<div class="banner">
  <span class="motif-word hindi" style="left:52px;top:14px;font-size:46px;">भीड</span>
  <span class="motif-word hanzi" style="left:176px;top:8px;font-size:46px;">众包</span>
  <span class="motif-word latin" style="left:374px;top:12px;font-size:36px;">karamihan ng tao</span>
  <span class="motif-word hindi" style="left:590px;top:18px;font-size:38px;">भीड</span>
  <span class="motif-word hanzi" style="left:760px;top:36px;font-size:46px;">众包</span>
  <span class="motif-word hanzi" style="left:1010px;top:6px;font-size:54px;">众包</span>
  <span class="motif-word latin" style="left:700px;top:118px;font-size:28px;">karamihan ng tao</span>
  <span class="motif-word hindi" style="left:950px;top:92px;font-size:30px;">भीड</span>
  <span class="motif-word hanzi" style="left:610px;top:92px;font-size:26px;">众包</span>
  <span class="motif-word hindi" style="left:690px;top:188px;font-size:24px;">भीड</span>

  <div class="hands-area" role="img" aria-label="Faint silhouettes of many raised hands"></div>

  <svg class="chart" width="1200" height="450" viewBox="0 0 1200 450" aria-hidden="true">
    <defs>
      <linearGradient id="growthFill" x1="0" y1="0" x2="0" y2="1">
        <stop offset="0" stop-color="var(--chart-fill-top)"/>
        <stop offset="1" stop-color="var(--chart-fill-bottom)"/>
      </linearGradient>
    </defs>
    <path d="M420 450 L491 411 Q580 385 666 371 Q800 360 919 349 Q1060 325 1149 279 Q1180 240 1200 165 L1200 450 Z" fill="url(#growthFill)"/>
    <path d="M420 450 L491 411 Q580 385 666 371 Q800 360 919 349 Q1060 325 1149 279 Q1180 240 1200 165" fill="none" stroke="var(--brand-red)" stroke-width="5" stroke-linejoin="round"/>
    <g fill="var(--brand-red)" stroke="var(--white)" stroke-width="3">
      <circle cx="491" cy="411" r="14"/>
      <circle cx="666" cy="371" r="14"/>
      <circle cx="919" cy="349" r="14"/>
      <circle cx="1149" cy="279" r="14"/>
    </g>
  </svg>

  <div class="emblem" role="img" aria-label="Round Asian mandala ornament"></div>

  <h1 class="title title-main">Asia's</h1>
  <h2 class="title title-sub">secret crowdsourcing boom</h2>

  <div class="subtitle-box">
    <span class="subtitle-number">5</span>
    <span class="subtitle-text">Things You Didn't Know About Crowdsourcing in Asia</span>
  </div>
</div>
</body>
</html>
```